Real Estate Open House & For Sale Signage

I am designing brand new signs for my real estate company. All I have so far are my logo and a business card design. I would like to have designed two different signs, 1. Open House directional sign, 2. For Sale Company sign. Both signs need to will be eye catching from the street, easy to read, identifiable and memorable.

Target Market(s)

Males & females, Ages between 30-65, affluent, educated, professionals.

Industry/Entity Type

Real Estate

Font styles to use
Serif
Sans Serif

Colors
33b8a4
34a7d8
acd137
3277b5

Requirements
Must have
• Must have my company logo & real estate license number visible on the sign. Must be easily visible and eye catching from a moving vehicle. Must have a professional and trustworthy appeal. Must bring to mind real estate.
Nice to have
• Image or icon that will denote real estate and be known as a part of my company identity and marketing theme.
Should not have
• Attached is a feeble attempt at creating my For Sale sign. The information on the sign is accurate, but the design is not appealing to me at all. It feels very amateurish.

```html
<!DOCTYPE html>
<html lang="en">
<head>
<meta charset="utf-8">
<title>For Sale Sign – Kailua Harbor Realty</title>
<link rel="stylesheet" href="https://fonts.googleapis.com/css2?family=Tinos:wght@400;700&family=Montserrat:wght@500;600&display=swap">
<style>
  :root {
    --backdrop: #e9eaec;
    --sign-white: #ffffff;
    --roof-grey: #5b5b5e;
    --headline-grey: #58585a;
    --accent-green: #acd137;
    --tagline-blue: #3277b5;
    --ink: #1e1e1e;
  }
  * { margin: 0; padding: 0; box-sizing: border-box; }
  html, body {
    width: 1200px; height: 1030px; overflow: hidden;
    background: var(--backdrop);
  }
  .sign {
    position: absolute; left: 30px; top: 80px;
    width: 1140px; height: 870px;
    background: var(--sign-white);
    overflow: hidden;
    box-shadow: 0 6px 24px rgba(0,0,0,.18);
  }
  .sign-roof { position: absolute; inset: 0; width: 1140px; height: 870px; }
  .brand {
    position: absolute; top: 318px; left: 0; width: 100%;
    display: flex; justify-content: center; align-items: center; gap: 14px;
    font-family: "Montserrat", sans-serif; font-weight: 600;
    font-size: 34px; letter-spacing: 4px; color: var(--accent-green);
  }
  .brand-dot {
    width: 22px; height: 22px; border-radius: 50%;
    background: var(--accent-green);
  }
  .headline {
    position: absolute; top: 368px; left: 0; width: 100%;
    text-align: center;
    font-family: "Tinos", serif; font-weight: 700;
    font-size: 190px; line-height: 1; letter-spacing: 2px;
    color: var(--headline-grey);
  }
  .tagline {
    position: absolute; top: 572px; left: 0; width: 100%;
    text-align: center;
    font-family: "Tinos", serif; font-weight: 400;
    font-size: 42px; letter-spacing: 7px;
    color: var(--tagline-blue);
  }
  .agent-name {
    position: absolute; top: 636px; left: 0; width: 100%;
    text-align: center;
    font-family: "Tinos", serif; font-size: 50px;
    color: var(--ink);
  }
  .phone-band {
    position: absolute; top: 712px; left: 0; width: 100%; height: 128px;
    background: var(--accent-green);
    display: flex; align-items: center; justify-content: center; gap: 60px;
  }
  .phone-icon { width: 92px; height: 92px; }
  .phone-number {
    font-family: "Tinos", serif; font-weight: 700;
    font-size: 112px; line-height: 1; color: var(--sign-white);
  }
  .license {
    position: absolute; right: 36px; bottom: 4px;
    font-family: "Tinos", serif; font-size: 24px;
    color: var(--headline-grey);
  }
</style>
</head>
<body>
  <main class="sign">
    <svg class="sign-roof" viewBox="0 0 1140 870" aria-hidden="true">
      <rect x="0" y="0" width="1140" height="330" fill="var(--roof-grey)"/>
      <polygon points="0,270 600,150 1140,330 1140,340 600,178 0,282" fill="var(--accent-green)"/>
      <polygon points="0,282 600,178 1140,340 1140,870 0,870" fill="var(--sign-white)"/>
    </svg>

    <div class="brand"><span class="brand-dot"></span>KAILUA HARBOR REALTY LLC</div>

    <h1 class="headline">FOR SALE</h1>
    <p class="tagline">YOUR NEIGHBORHOOD SPECIALIST</p>
    <p class="agent-name">Leilani Brooks</p>

    <div class="phone-band">
      <svg class="phone-icon" viewBox="0 0 92 92" aria-hidden="true">
        <circle cx="46" cy="46" r="41" fill="none" stroke="var(--sign-white)" stroke-width="6"/>
        <path d="M32 24c3-2 6-1 7 2l4 9c1 2 0 4-2 5l-3 2c2 6 7 11 13 13l2-3c1-2 3-3 5-2l9 4c3 1 4 4 2 7l-3 4c-2 3-6 4-10 3-14-4-25-15-29-29-1-4 0-8 3-10z" fill="var(--sign-white)"/>
      </svg>
      <span class="phone-number">(808) 555-0147</span>
    </div>

    <p class="license">RB-20415</p>
  </main>
</body>
</html>
```